Clean, Throwback Album Art needed

I'm looking for album art for an Indie Rock EP titled "The Farther Meridian". The artist name is "Colin Vasquez"

I'm looking for a design that's wistful and nostalgic, but not depressing. I'm more interested in creative patterns and color combinations than anything else. I've uploaded two examples of album art I really like.

Please no stock images.

In addition to the album art, I will also need two variants of a back cover created in a complementary style- one with a track listing and one with marketing copy (e.g. Free download available at ___ ). These back covers do not have to be incredibly detailed, but can't just be text overlaid on top of of the front cover.

Details for back cover (track names, credits, etc.) will be provided to whoever submits the winning front cover design.

Requirements
Should not have
• No stock images. I need to know that I fully own the copyright to whatever work is produced.

```html
<!DOCTYPE html>
<html lang="en">
<head>
<meta charset="utf-8">
<title>Colin Vasquez — The Farther Meridian</title>
<link rel="stylesheet" href="https://fonts.googleapis.com/css2?family=Nanum+Pen+Script&family=Josefin+Sans:wght@300&display=swap">
<style>
  :root {
    --bg-light: #c08b55;
    --bg-mid: #8f5326;
    --bg-dark: #3d1704;
    --frame: #ffffff;
    --accent: #f2c617;
    --artist-ink: #3a3a3a;
    --title-ink: #ffffff;
  }
  html, body {
    margin: 0;
    padding: 0;
    overflow: hidden;
    background: var(--bg-dark);
  }
  .cover {
    position: relative;
    width: 1200px;
    height: 1200px;
    overflow: hidden;
  }
  .cover__texture {
    position: absolute;
    inset: 0;
    background:
      radial-gradient(ellipse 55% 50% at 50% 48%, var(--bg-light) 0%, #a86d3a 40%, var(--bg-mid) 70%, var(--bg-dark) 100%);
  }
  .cover__frame {
    position: absolute;
    left: 50px;
    top: 50px;
    width: 1100px;
    height: 1100px;
    box-sizing: border-box;
    border: 2px solid var(--frame);
  }
  .artist {
    position: absolute;
    left: 190px;
    top: 532px;
    width: 790px;
    height: 140px;
  }
  .artist__bar {
    position: absolute;
    top: 0;
    width: 4px;
    height: 140px;
    background: var(--accent);
  }
  .artist__bar--left { left: 0; }
  .artist__bar--right { right: 0; }
  .artist__name {
    position: absolute;
    left: 0;
    right: 0;
    top: 18px;
    margin: 0;
    text-align: center;
    font-family: "Nanum Pen Script", cursive;
    font-weight: 400;
    font-size: 118px;
    line-height: 1;
    color: var(--artist-ink);
    text-transform: lowercase;
    letter-spacing: 0.01em;
    -webkit-text-stroke: 2px var(--artist-ink);
  }
  .title-rule {
    position: absolute;
    left: 466px;
    top: 972px;
    width: 268px;
    height: 3px;
    background: var(--accent);
  }
  .album-title {
    position: absolute;
    left: 0;
    right: 0;
    top: 1006px;
    margin: 0;
    text-align: center;
    font-family: "Josefin Sans", sans-serif;
    font-weight: 300;
    font-size: 29px;
    line-height: 1;
    letter-spacing: 0.95em;
    padding-left: 0.95em;
    color: var(--title-ink);
    text-transform: uppercase;
  }
</style>
</head>
<body>
  <main class="cover">
    <div class="cover__texture" role="img" aria-label="Warm brown weathered wall texture with a lighter amber glow in the centre"></div>
    <div class="cover__frame"></div>

    <div class="artist">
      <span class="artist__bar artist__bar--left"></span>
      <h1 class="artist__name">colin vasquez</h1>
      <span class="artist__bar artist__bar--right"></span>
    </div>

    <div class="title-rule"></div>
    <h2 class="album-title">The Farther Meridian</h2>
  </main>
</body>
</html>
```